Kettlebrook Holdings, LLC. What we do is rehab homes for the purpose of flipping them and also have a rental portfolio as well.

We do not have a logo so that will need to be part of the design process

Would like, if possible to have a house or something with housing or remodeling incorporated in design.

Industry/Entity Type

Rental

Contact Information for Business Card

Dale Varnum
912 thistle Ct.
Marlow, il 60499
847-555-0143
Fax 630-555-0178

```html
<!DOCTYPE html>
<html lang="en">
<head>
<meta charset="utf-8">
<title>Kettlebrook Holdings, LLC — Business Card</title>
<link rel="stylesheet" href="https://fonts.googleapis.com/css2?family=Open+Sans:wght@400;600;700&display=swap">
<style>
  :root {
    --page-bg: #b4b4b4;
    --card-white: #ffffff;
    --card-black: #16181b;
    --card-black-deep: #0b0c0e;
    --brand-blue: #2a4ea6;
    --brand-blue-dark: #1b3478;
    --silver: #c9ccd2;
    --text-light: #f2f2f2;
    --divider: #8a8d92;
  }
  * { margin: 0; padding: 0; box-sizing: border-box; }
  html, body {
    width: 1200px; height: 900px; overflow: hidden;
    background: var(--page-bg);
    font-family: "Open Sans", Arial, sans-serif;
  }
  .business-card {
    position: absolute;
    left: 160px; top: 170px;
    width: 880px; height: 560px;
    border-radius: 42px;
    overflow: hidden;
    background: var(--card-white);
    box-shadow: 0 18px 40px rgba(0,0,0,0.25);
  }
  .brand-area {
    position: absolute; left: 0; top: 0;
    width: 100%; height: 316px;
    display: flex; align-items: center; justify-content: center;
    gap: 18px;
  }
  .brand-mark {
    width: 30px; height: 30px;
    background: var(--brand-blue);
  }
  .brand-name {
    font-size: 44px; font-weight: 600;
    color: var(--brand-blue-dark);
    letter-spacing: 1px;
  }
  .accent-band {
    position: absolute; left: 0; top: 316px;
    width: 100%; height: 18px;
    background: linear-gradient(90deg, var(--brand-blue-dark), var(--brand-blue) 50%, var(--brand-blue-dark));
  }
  .silver-rule {
    position: absolute; left: 0; top: 334px;
    width: 100%; height: 5px;
    background: linear-gradient(180deg, #ffffff, var(--silver) 60%, #7d8188);
  }
  .contact-panel {
    position: absolute; left: 0; top: 339px;
    width: 100%; height: 221px;
    background: linear-gradient(180deg, var(--card-black), var(--card-black-deep));
  }
  .person {
    position: absolute; right: 395px; top: 60px;
    text-align: right;
  }
  .person-name {
    font-size: 32px; font-weight: 700;
    color: var(--brand-blue);
    line-height: 1.2;
  }
  .person-title {
    font-size: 23px; font-weight: 400;
    color: var(--text-light);
    line-height: 1.3;
  }
  .divider {
    position: absolute; left: 510px; top: 26px;
    width: 2px; height: 160px;
    background: var(--divider);
  }
  .contact-list {
    position: absolute; left: 535px; top: 20px;
    list-style: none;
  }
  .contact-list li {
    display: flex; align-items: center;
    height: 31px;
    font-size: 21px; color: var(--text-light);
    white-space: nowrap;
  }
  .contact-list .icon {
    width: 24px; height: 24px; margin-right: 8px;
    flex: none; fill: var(--brand-blue);
  }
  .contact-list .no-icon { margin-left: 32px; }
</style>
</head>
<body>
  <main class="business-card">
    <header class="brand-area">
      <span class="brand-mark"></span>
      <span class="brand-name">Kettlebrook Holdings, LLC</span>
    </header>
    <div class="accent-band"></div>
    <div class="silver-rule"></div>
    <section class="contact-panel">
      <div class="person">
        <p class="person-name">Dale Varnum</p>
        <p class="person-title">manager</p>
      </div>
      <div class="divider"></div>
      <ul class="contact-list">
        <li>
          <svg class="icon" viewBox="0 0 24 24" aria-hidden="true"><path d="M6.6 10.8a15 15 0 0 0 6.6 6.6l2.2-2.2c.3-.3.7-.4 1-.2 1.1.4 2.300.6 3.6.6.6 0 1 .4 1 1V20c0 .6-.4 1-1 1A17 17 0 0 1 3 4c0-.6.4-1 1-1h3.5c.6 0 1 .4 1 1 0 1.3.2 2.5.6 3.6.1.3 0 .7-.2 1z"/></svg>
          847-555-0143
        </li>
        <li>
          <svg class="icon" viewBox="0 0 24 24" aria-hidden="true"><path d="M6 2h10l2 2v5H6z M3 10h18a1 1 0 0 1 1 1v7a1 1 0 0 1-1 1h-3v3H6v-3H3a1 1 0 0 1-1-1v-7a1 1 0 0 1 1-1zm5 6v4h8v-4z"/></svg>
          630-555-0178
        </li>
        <li>
          <svg class="icon" viewBox="0 0 24 24" aria-hidden="true"><path d="M12 3l10 9h-3v9h-5v-6h-4v6H5v-9H2z"/></svg>
          912 thistle Ct.
        </li>
        <li>
          <svg class="icon" viewBox="0 0 24 24" aria-hidden="true"><path d="M2 9l10-6 10 6v11a1 1 0 0 1-1 1H3a1 1 0 0 1-1-1zm2 1.2V19h16v-8.8l-8 5z"/></svg>
          Marlow, il 60499
        </li>
        <li><span class="no-icon">dalevarnum@kettlemail.net</span></li>
      </ul>
    </section>
  </main>
</body>
</html>
```